Seasoned logs and kindling for sale

producing firewood from beech,ash,oak and silver birch,
Kindling is produce from a variety of seasoned softwoods

Industry/Entity Type

Firewood

Contact Information for Business Card

peter Calloway 07831226904
alan Frickley 07854317620
e-mail,peterc817@mailbrook.example

```html
<!DOCTYPE html>
<html lang="en">
<head>
<meta charset="utf-8">
<title>Seasoned Logs &amp; Kindling – Business Card</title>
<link href="https://fonts.googleapis.com/css2?family=Oswald:wght@700&family=Yanone+Kaffeesatz:wght@400&family=Roboto:wght@700&family=Montserrat:wght@400&display=swap" rel="stylesheet">
<style>
  :root {
    --headline-lime: #b6e11f;
    --wood-dark: #4a4540;
    --wood-mid: #6a645c;
    --badge-tan: #c19a5b;
    --divider-maroon: #55142a;
    --contact-brown: #99624f;
    --text-white: #ffffff;
    --text-black: #111111;
  }
  html, body {
    margin: 0;
    padding: 0;
    overflow: hidden;
    background: #ffffff;
  }
  .card {
    position: relative;
    width: 1200px;
    height: 791px;
    overflow: hidden;
    background: var(--contact-brown);
  }
  .wood-photo {
    position: absolute;
    left: 0; top: 0;
    width: 1200px; height: 447px;
    background: linear-gradient(180deg, var(--wood-mid) 0%, var(--wood-dark) 100%);
  }
  .headline {
    position: absolute;
    left: 0; top: 22px;
    width: 1210px;
    margin: 0;
    text-align: center;
    font-family: "Oswald", sans-serif;
    font-weight: 700;
    font-size: 73px;
    letter-spacing: -2px;
    line-height: 1.2;
    color: var(--headline-lime);
    text-shadow: 1px 1px 2px rgba(0,0,0,0.35);
  }
  .wood-badge {
    position: absolute;
    left: 45px; top: 172px;
    width: 343px; height: 198px;
    box-sizing: border-box;
    padding: 12px 0 0 13px;
    border-radius: 12px;
    background: var(--badge-tan);
    font-family: "Yanone Kaffeesatz", sans-serif;
    font-size: 42px;
    line-height: 62px;
    letter-spacing: 3.5px;
    color: var(--text-white);
    margin: 0;
    white-space: nowrap;
  }
  .divider {
    position: absolute;
    left: 0; top: 447px;
    width: 1200px; height: 15px;
    background: var(--divider-maroon);
  }
  .contact {
    position: absolute;
    top: 495px;
  }
  .contact--left { left: 143px; }
  .contact--right { left: 765px; }
  .contact__name {
    margin: 0;
    font-family: "Roboto", sans-serif;
    font-weight: 700;
    font-size: 50px;
    line-height: 64px;
    color: var(--text-white);
    white-space: nowrap;
  }
  .contact__phone {
    margin: 0 0 0 15px;
    font-family: "Montserrat", sans-serif;
    font-size: 39px;
    line-height: 56px;
    letter-spacing: 3px;
    color: var(--text-black);
  }
  .contact--right .contact__phone { margin-left: 2px; }
  .email {
    position: absolute;
    left: 0; top: 690px;
    width: 1195px;
    margin: 0;
    text-align: center;
    font-family: "Montserrat", sans-serif;
    font-size: 40px;
    line-height: 56px;
    color: var(--text-black);
  }
</style>
</head>
<body>
  <main class="card">
    <div class="wood-photo" role="img" aria-label="Photograph of weathered timber with a knot hole"></div>
    <h1 class="headline">SEASONED LOGS &amp; KINDLING FOR SALE</h1>
    <p class="wood-badge">Producing Firewood<br>from Beech, Ash,<br>Oak&amp; Silver Birch</p>
    <div class="divider"></div>
    <section class="contact contact--left">
      <p class="contact__name">Peter Calloway</p>
      <p class="contact__phone">07831226904</p>
    </section>
    <section class="contact contact--right">
      <p class="contact__name">Alan Frickley</p>
      <p class="contact__phone">07854317620</p>
    </section>
    <p class="email">peterc817@mailbrook.example</p>
  </main>
</body>
</html>
```